CD Cover Design Project

I am a lady portrait photographer looking to have a cd cover designed and to maybe use the design to also print some postcards and labels etc.
I do child portraits mainly, also some family photography.
My clients are mums and women.My photography is described as spirited, enchanting, intuitive, but with a modern twist.
**Please do not use my pictures in the design** I give these cd covers to my clients and they do not want to see other peoples children on the cd cover.
I would like to use simple graphics, funky and happy and feminine. My logo has hearts, but I also like dots. The colours that I require are the same as my logo which I included -red and lime.
I am open to suggestions. Happy to chat.
Melinda Farrow
my blog is www.melindafarrow-example.com
my website is www.melindafarrow-example.com.au

Industry/Entity Type

Photographer

Requirements
Must have
• Colours to match my logo.
Should not have
• My photographs on the cd cover. My clients do not want to see other peoples children on their stationary. Just graphics thanks.

```html
<!DOCTYPE html>
<html lang="en">
<head>
<meta charset="utf-8">
<title>Every Little Wonder – Melinda Farrow Photography</title>
<link rel="stylesheet" href="https://fonts.googleapis.com/css2?family=Arimo:wght@400&display=swap">
<style>
  :root {
    --paper: #ffffff;
    --ink-grey: #5e5e5e;
    --lime: #a8cf3a;
    --lime-soft: #e9f4c8;
    --lime-pale: #f5faea;
    --red: #d8262f;
    --red-soft: #f3a1a4;
  }
  html, body {
    margin: 0;
    padding: 0;
    width: 1200px;
    height: 1200px;
    overflow: hidden;
    background: var(--paper);
  }
  .cover {
    position: relative;
    width: 1200px;
    height: 1200px;
    background: var(--paper);
    font-family: "Arimo", Arial, sans-serif;
    color: var(--ink-grey);
  }
  .site-url {
    position: absolute;
    top: 120px;
    left: 0;
    width: 100%;
    margin: 0;
    text-align: center;
    font-size: 20px;
    line-height: 1;
    letter-spacing: 0.22em;
  }
  .artwork {
    position: absolute;
    top: 207px;
    left: 207px;
    width: 790px;
    height: 790px;
    display: block;
  }
  .artwork .ground { fill: var(--lime-pale); }
  .artwork .dot-lime { fill: var(--lime); }
  .artwork .dot-lime-soft { fill: var(--lime-soft); }
  .artwork .dot-red { fill: var(--red); }
  .artwork .dot-red-soft { fill: var(--red-soft); }
  .artwork .heart-red { fill: var(--red); }
  .artwork .heart-lime { fill: var(--lime); }
  .brand {
    position: absolute;
    top: 1050px;
    left: 0;
    width: 100%;
    text-align: center;
  }
  .brand-name {
    margin: 0;
    font-size: 50px;
    font-weight: 400;
    line-height: 1;
    color: var(--ink-grey);
  }
  .brand-tagline {
    margin: 14px 0 0;
    font-size: 21px;
    line-height: 1;
    letter-spacing: 0.02em;
    color: var(--ink-grey);
  }
</style>
</head>
<body>
  <main class="cover">
    <p class="site-url">WWW.MELINDAFARROW-EXAMPLE.COM.AU</p>

    <svg class="artwork" viewBox="0 0 790 790" aria-hidden="true">
      <rect class="ground" x="0" y="0" width="790" height="790"/>
      <!-- soft background dots -->
      <circle class="dot-lime-soft" cx="140" cy="150" r="110"/>
      <circle class="dot-lime-soft" cx="640" cy="620" r="140"/>
      <circle class="dot-red-soft" cx="600" cy="170" r="70" opacity="0.6"/>
      <circle class="dot-red-soft" cx="170" cy="640" r="60" opacity="0.6"/>
      <!-- lime dots -->
      <circle class="dot-lime" cx="395" cy="395" r="150"/>
      <circle class="dot-lime" cx="120" cy="380" r="34"/>
      <circle class="dot-lime" cx="680" cy="360" r="46"/>
      <circle class="dot-lime" cx="300" cy="120" r="22"/>
      <circle class="dot-lime" cx="520" cy="690" r="28"/>
      <circle class="dot-lime" cx="250" cy="560" r="16"/>
      <circle class="dot-lime" cx="720" cy="90" r="14"/>
      <circle class="dot-lime" cx="70" cy="720" r="20"/>
      <!-- red dots -->
      <circle class="dot-red" cx="230" cy="260" r="26"/>
      <circle class="dot-red" cx="570" cy="540" r="38"/>
      <circle class="dot-red" cx="470" cy="100" r="16"/>
      <circle class="dot-red" cx="90" cy="520" r="12"/>
      <circle class="dot-red" cx="350" cy="700" r="20"/>
      <circle class="dot-red" cx="730" cy="480" r="12"/>
      <circle class="dot-red" cx="620" cy="280" r="10"/>
      <!-- hearts -->
      <path class="heart-red" transform="translate(395 410) scale(3)" d="M0 18 C-26 0 -22 -20 -10 -20 C-4 -20 0 -14 0 -10 C0 -14 4 -20 10 -20 C22 -20 26 0 0 18 Z"/>
      <path class="heart-red" transform="translate(160 470) scale(1.1)" d="M0 18 C-26 0 -22 -20 -10 -20 C-4 -20 0 -14 0 -10 C0 -14 4 -20 10 -20 C22 -20 26 0 0 18 Z"/>
      <path class="heart-lime" transform="translate(560 220) scale(1.3)" d="M0 18 C-26 0 -22 -20 -10 -20 C-4 -20 0 -14 0 -10 C0 -14 4 -20 10 -20 C22 -20 26 0 0 18 Z"/>
      <path class="heart-red" transform="translate(660 720) scale(0.9)" d="M0 18 C-26 0 -22 -20 -10 -20 C-4 -20 0 -14 0 -10 C0 -14 4 -20 10 -20 C22 -20 26 0 0 18 Z"/>
    </svg>

    <div class="brand">
      <h1 class="brand-name">Every Little Wonder</h1>
      <p class="brand-tagline">PHOTOGRAPHY BY MELINDA FARROW</p>
    </div>
  </main>
</body>
</html>
```